Marlowe Coverage Group Circle of Services Marketing Flyer

Business flyer that describes the services offered by an Employee Benefits insurance agency. Flyer will be distributed to current and prospective clients and should visually be professional, simple and keep to current logo and color scheme. The flyer will be used in various situations to promote Marlowe Coverage to prospective clients and also in general marketing to current clients. The objective is to show a busy business owner in the middle that does not have time to worry and deal with the headaches of all of the services listed that Marlowe Coverage provides.

Target Market(s)

Small and Large employer groups looking for solutions and to modernize the way they purchase and manage employee benefits.

Industry/Entity Type

Health Insurance

Font styles to use
Sans Serif

Colors
33a6d7
0292cd
85cae6

Requirements
Must have
• In the middle I would like a picture of a businessperson that looks busy and stressed out. The "Circle of Services" should shoot out from there all around.
• The services should be listed as:
• 1) Employee Benefits - Health Insurance, Dental, Vision, Life, Disability, Voluntary Life, Critical Illness, Cancer, Accident
• 2) Payroll Services
• 3) Compliance Services - ACA Compliance, ERISA, 1094/1095 Reporting
• 4) Human Resources and Web Based Benefits Enrollment & Administration Systems
• 5) Personal Planning
Nice to have
• website listed - www.marlowecoverage.example
• Phone Numbers:
• Arkansas 555.318.7720
• Tennessee 555.642.9035
Should not have
• Cartoon figures

```html
<!DOCTYPE html>
<html lang="en">
<head>
<meta charset="utf-8">
<title>Marlowe Coverage Group – Circle of Services</title>
<link rel="stylesheet" href="https://fonts.googleapis.com/css2?family=Open+Sans:wght@400;600&family=PT+Sans+Narrow:wght@400;700&display=swap">
<style>
  :root {
    --brand-blue: #0292cd;
    --brand-mid: #33a6d7;
    --brand-light: #85cae6;
    --band-deep: #0a6a99;
    --ink: #333a40;
    --ink-soft: #4a5055;
    --paper: #ffffff;
    --paper-shade: #e4e6e8;
  }
  * { box-sizing: border-box; margin: 0; padding: 0; }
  html, body { width: 947px; height: 1200px; overflow: hidden; background: #f2f2f2; }
  .flyer {
    position: relative;
    width: 947px;
    height: 1200px;
    overflow: hidden;
    background: radial-gradient(ellipse at 50% 45%, var(--paper) 30%, var(--paper-shade) 100%);
    font-family: "Open Sans", sans-serif;
    color: var(--ink);
  }
  .top-swoosh { position: absolute; left: 0; top: 0; width: 947px; height: 240px; }
  .brand-name {
    position: absolute;
    left: 42px;
    top: 62px;
    font-family: "Open Sans", sans-serif;
    font-weight: 600;
    font-size: 36px;
    letter-spacing: -0.5px;
    color: var(--ink-soft);
  }
  .hero-photo {
    position: absolute;
    left: 0;
    top: 325px;
    width: 947px;
    height: 598px;
    background:
      radial-gradient(ellipse at 50% 55%, #b9b2aa 0%, #d6d4d1 35%, transparent 65%),
      linear-gradient(180deg, #eef1f3 0%, #dfe3e6 60%, #cfd3d6 100%);
  }
  .service {
    position: absolute;
    width: 208px;
    height: 208px;
    border-radius: 50%;
    background: var(--paper);
    border: 9px solid var(--brand-light);
    box-shadow: 0 4px 10px rgba(0,0,0,0.28);
    display: flex;
    flex-direction: column;
    align-items: center;
    justify-content: center;
    text-align: center;
    padding: 0 18px;
  }
  .service-title {
    font-family: "PT Sans Narrow", sans-serif;
    font-weight: 700;
    font-size: 29px;
    line-height: 1.05;
    color: var(--ink);
    text-transform: uppercase;
  }
  .service-title.small {
    font-size: 16px;
    line-height: 1.35;
  }
  .service-detail {
    margin-top: 12px;
    font-size: 11px;
    line-height: 1.3;
    color: var(--ink-soft);
  }
  .service--benefits   { left: 369px; top: 183px; }
  .service--personal   { left: 31px;  top: 363px; }
  .service--payroll    { left: 715px; top: 363px; }
  .service--hr         { left: 183px; top: 810px; }
  .service--compliance { left: 568px; top: 810px; }
  .bottom-band { position: absolute; left: 0; top: 1040px; width: 947px; height: 160px; }
  .contact {
    position: absolute;
    left: 0;
    width: 947px;
    text-align: center;
    color: var(--paper);
  }
  .contact-web { top: 1102px; font-weight: 600; font-size: 30px; letter-spacing: 0.2px; }
  .contact-phones { top: 1148px; font-size: 20px; }
  .contact-phones .divider { margin: 0 10px; }
</style>
</head>
<body>
<main class="flyer">
  <svg class="top-swoosh" viewBox="0 0 947 240" aria-hidden="true">
    <defs>
      <linearGradient id="swooshFill" x1="0" y1="0" x2="1" y2="0">
        <stop offset="0" stop-color="#33a6d7"/>
        <stop offset="0.6" stop-color="#2a86b5"/>
        <stop offset="1" stop-color="#1c5f86"/>
      </linearGradient>
    </defs>
    <path d="M0 185 C 230 170, 460 120, 608 0 L 600 0 C 450 100, 230 150, 0 150 Z" fill="#d9e9f2"/>
    <path d="M0 188 C 240 176, 470 128, 612 0 L 602 0 C 450 110, 240 158, 0 190 Z" fill="url(#swooshFill)"/>
    <path d="M0 190 C 250 170, 480 120, 612 0 C 490 140, 260 210, 0 232 Z" fill="url(#swooshFill)"/>
  </svg>

  <div class="brand-name">Marlowe Coverage Group</div>

  <div class="hero-photo" role="img" aria-label="Photo of a stressed businessman holding his head at a laptop while coworkers hand him papers, a phone and a pen"></div>

  <section class="service service--benefits">
    <h2 class="service-title">Employee<br>Benefits</h2>
    <p class="service-detail">Health Insurance, Dental, Vision, Life, Disability, Voluntary Life, Critical Illness, Cancer, Accident</p>
  </section>

  <section class="service service--personal">
    <h2 class="service-title">Personal<br>Planning</h2>
  </section>

  <section class="service service--payroll">
    <h2 class="service-title">Payroll<br>Services</h2>
  </section>

  <section class="service service--hr">
    <h2 class="service-title small">Human Resources<br>and Web Based Benefits<br>Enrollment &amp; Administration<br>Systems</h2>
  </section>

  <section class="service service--compliance">
    <h2 class="service-title">Compliance<br>Services</h2>
    <p class="service-detail">ACA Compliance, ERISA,<br>1094/1095 Reporting</p>
  </section>

  <svg class="bottom-band" viewBox="0 0 947 160" aria-hidden="true">
    <defs>
      <linearGradient id="bandFill" x1="0" y1="0" x2="1" y2="0">
        <stop offset="0" stop-color="#0a6a99"/>
        <stop offset="0.5" stop-color="#0292cd"/>
        <stop offset="1" stop-color="#0a6a99"/>
      </linearGradient>
    </defs>
    <path d="M0 48 C 300 -8, 650 -8, 947 48 L 947 160 L 0 160 Z" fill="#bfe3f2"/>
    <path d="M0 68 C 300 14, 650 14, 947 68 L 947 160 L 0 160 Z" fill="url(#bandFill)"/>
  </svg>

  <p class="contact contact-web">WWW.MARLOWECOVERAGE.EXAMPLE</p>
  <p class="contact contact-phones">Arkansas 555.318.7720<span class="divider">|</span>Tennessee 555.642.9035</p>
</main>
</body>
</html>
```